Bully breed rescue website

I need a website for my bully breed rescue. We rescue bully breeds from up and down the east coast of the United States and train them as service dogs for people with limited mobility disabilities. I don't want a lot of white space. I want it to be modern and slick and colorful and still look professional. I want it to be different and have a lot of wow factor. I linked a copy of my logo.

Number of Pages Required

5+ page

Font styles to use
Sans Serif

Colors

Designer to choose colors to be used in the design.

Requirements
Must have
• Moving aspects. Blog and ecommerce.
• 1.) Home page
• 2.) Services- something modular
• 3.) About US
• 4.) Blog
• 5.) Application page
• 6.) Donation page
• 7.) Contact Us
Nice to have
• Large Slider of photos on home page
• vertical menu bar
Should not have
• Lots of white space. Dont want it to look like a template or any other site

```html
<!DOCTYPE html>
<html lang="en">
<head>
<meta charset="utf-8">
<title>Our Services – Stand Tall Rescue</title>
<link rel="stylesheet" href="https://fonts.googleapis.com/css2?family=Roboto:wght@400;500;700&display=swap">
<style>
:root{
  --yellow:#f6cf3b;
  --white:#ffffff;
  --ink:#111111;
  --footer:#ececec;
  --red:#e8262b;
  --gold:#f3c92d;
  --green:#4c9a12;
  --grass:#4f8f2c;
  --coat:#8a5a34;
  --dark:#121110;
}
*{box-sizing:border-box;margin:0;padding:0}
html,body{width:1200px;height:2639px;overflow:hidden}
body{position:relative;font-family:'Roboto',Arial,sans-serif;background:var(--footer);color:var(--ink)}
.abs{position:absolute}
.icon-defs{position:absolute;width:0;height:0;overflow:hidden}
.hero-photo{left:0;top:0;width:1200px;height:660px;
  background:
    radial-gradient(ellipse 300px 240px at 420px 470px,rgba(190,90,100,.55),transparent 70%),
    radial-gradient(ellipse 520px 420px at 560px 240px,#e9e2d6 0%,#b89a78 30%,#7b5638 55%,transparent 80%),
    linear-gradient(160deg,#9fc27c 0%,var(--grass) 45%,#3d7421 100%)}
.logo{left:40px;top:66px;display:flex;align-items:center;gap:12px}
.logo-dot{width:44px;height:44px;border-radius:50%;background:var(--white)}
.logo-name{font-weight:700;font-size:24px;color:var(--white);letter-spacing:.5px}
.menu-btn{left:1096px;top:51px;width:60px;height:60px;border:2px solid var(--ink);border-radius:50%;display:flex;flex-direction:column;justify-content:center;align-items:center;gap:6px}
.menu-btn span{display:block;width:26px;height:3px;background:var(--ink);border-radius:2px}
.page-title{left:0;top:290px;width:1200px;text-align:center;font-weight:700;font-size:64px;color:var(--white);text-shadow:0 3px 8px rgba(0,0,0,.5)}
.wave{left:0;width:1200px}
.services{left:0;top:655px;width:1200px;height:1220px;background:var(--yellow)}
.grid{left:40px;top:702px;width:1120px;display:grid;grid-template-columns:repeat(4,271px);column-gap:12px;row-gap:82px}
.card{position:relative;height:289px;background:var(--white)}
.card-photo{height:199px;
  background:
    radial-gradient(ellipse 70px 80px at 75px 80px,#efe6da 0%,#c7a27c 45%,transparent 75%),
    radial-gradient(ellipse 80px 90px at 200px 110px,#b77a45 0%,#7e4f2c 55%,transparent 80%),
    var(--dark)}
.card-name{position:absolute;left:0;right:0;top:231px;text-align:center;font-weight:500;font-size:22px;line-height:28px}
.paw{position:absolute;display:block}
.paw.red{color:var(--red)}
.paw.gold{color:var(--gold)}
.paw.green{color:var(--green)}
.card .paw.red{left:2px;top:184px;width:54px;height:58px;transform:rotate(-25deg)}
.card .paw.gold{left:198px;top:166px;width:56px;height:58px;transform:rotate(20deg)}
.card .paw.green{left:164px;top:258px;width:58px;height:60px;transform:rotate(-15deg)}
.contact-photo{left:0;top:1760px;width:1200px;height:520px;
  background:
    radial-gradient(ellipse 260px 260px at 260px 2190px,transparent,transparent),
    radial-gradient(ellipse 300px 280px at 260px 220px,#f1ece4 0%,#c9a27c 35%,#8a5a34 60%,transparent 85%),
    radial-gradient(ellipse 380px 260px at 930px 260px,#a86e40 0%,#6e4326 55%,transparent 85%),
    linear-gradient(90deg,#2a1a10,#1a1210 50%,#3a2616)}
.contact-title{left:0;top:1882px;width:1200px;text-align:center;font-weight:700;font-size:35px;color:var(--white)}
.field{top:1983px;height:80px;border-radius:40px;background:rgba(255,255,255,.88);padding-left:30px;display:flex;align-items:center;font-size:17px;color:#555}
.field.name{left:106px;width:364px}
.field.email{left:495px;width:364px}
.submit{left:882px;top:1983px;width:213px;height:80px;border-radius:40px;background:var(--yellow);color:var(--white);font-weight:700;font-size:17px;display:flex;align-items:center;justify-content:center}
.info{top:2290px;width:240px;text-align:center}
.info h3{font-weight:500;font-size:28px;line-height:33px;margin-top:44px}
.info p{font-size:18px;line-height:28px;margin-top:8px}
.info .paw.gold{left:4px;top:19px;width:52px;height:54px;transform:rotate(-20deg)}
.info .paw.green{left:124px;top:-23px;width:54px;height:56px;transform:rotate(15deg)}
.info .paw.red{left:176px;top:24px;width:54px;height:56px;transform:rotate(20deg)}
.info-mail{left:60px}.info-hours{left:339px}.info-phone{left:623px}.info-email{left:904px}
.divider{left:40px;top:2469px;width:1120px;height:2px;background:linear-gradient(90deg,var(--red),var(--gold),var(--green))}
.copyright{left:0;top:2515px;width:1200px;text-align:center;font-size:14px;color:#444}
.social{left:506px;top:2547px;display:flex;gap:17px}
.social span{width:34px;height:34px;border-radius:50%;background:var(--gold)}
</style>
</head>
<body>
<svg class="icon-defs" aria-hidden="true">
  <symbol id="paw" viewBox="0 0 48 48">
    <path fill="currentColor" d="M24 22c-7 0-14 9-14 15 0 5 5 7 9 6 2 0 3-1 5-1s3 1 5 1c4 1 9-1 9-6 0-6-7-15-14-15z"/>
    <ellipse fill="currentColor" cx="8" cy="21" rx="4.2" ry="5.6" transform="rotate(-25 8 21)"/>
    <ellipse fill="currentColor" cx="17" cy="10" rx="4.6" ry="6.2" transform="rotate(-8 17 10)"/>
    <ellipse fill="currentColor" cx="31" cy="10" rx="4.6" ry="6.2" transform="rotate(8 31 10)"/>
    <ellipse fill="currentColor" cx="40" cy="21" rx="4.2" ry="5.6" transform="rotate(25 40 21)"/>
  </symbol>
</svg>
<div class="abs hero-photo" role="img" aria-label="Close-up photo of a happy bulldog lying in green grass"></div>
<div class="abs logo"><span class="logo-dot"></span><span class="logo-name">STAND TALL RESCUE</span></div>
<div class="abs menu-btn"><span></span><span></span><span></span></div>
<h1 class="abs page-title">OUR SERVICES</h1>
<div class="abs services"></div>
<svg class="abs wave" style="top:490px" width="1200" height="180" viewBox="0 490 1200 180">
  <path d="M0 635 C250 600 480 505 800 512 C1000 518 1100 600 1200 625 L1200 670 L0 670 Z" fill="var(--yellow)"/>
</svg>
<div class="abs grid">
  <div class="card"><div class="card-photo" role="img" aria-label="Photo of two bulldogs looking up"></div><svg class="paw red" aria-hidden="true"><use href="#paw"/></svg><svg class="paw gold" aria-hidden="true"><use href="#paw"/></svg><div class="card-name">Services Name</div><svg class="paw green" aria-hidden="true"><use href="#paw"/></svg></div>
  <div class="card"><div class="card-photo" role="img" aria-label="Photo of two bulldogs looking up"></div><svg class="paw red" aria-hidden="true"><use href="#paw"/></svg><svg class="paw gold" aria-hidden="true"><use href="#paw"/></svg><div class="card-name">Services Name</div><svg class="paw green" aria-hidden="true"><use href="#paw"/></svg></div>
  <div class="card"><div class="card-photo" role="img" aria-label="Photo of two bulldogs looking up"></div><svg class="paw red" aria-hidden="true"><use href="#paw"/></svg><svg class="paw gold" aria-hidden="true"><use href="#paw"/></svg><div class="card-name">Services Name</div><svg class="paw green" aria-hidden="true"><use href="#paw"/></svg></div>
  <div class="card"><div class="card-photo" role="img" aria-label="Photo of two bulldogs looking up"></div><svg class="paw red" aria-hidden="true"><use href="#paw"/></svg><svg class="paw gold" aria-hidden="true"><use href="#paw"/></svg><div class="card-name">Services Name</div><svg class="paw green" aria-hidden="true"><use href="#paw"/></svg></div>
  <div class="card"><div class="card-photo" role="img" aria-label="Photo of two bulldogs looking up"></div><svg class="paw red" aria-hidden="true"><use href="#paw"/></svg><svg class="paw gold" aria-hidden="true"><use href="#paw"/></svg><div class="card-name">Services Name</div><svg class="paw green" aria-hidden="true"><use href="#paw"/></svg></div>
  <div class="card"><div class="card-photo" role="img" aria-label="Photo of two bulldogs looking up"></div><svg class="paw red" aria-hidden="true"><use href="#paw"/></svg><svg class="paw gold" aria-hidden="true"><use href="#paw"/></svg><div class="card-name">Services Name</div><svg class="paw green" aria-hidden="true"><use href="#paw"/></svg></div>
  <div class="card"><div class="card-photo" role="img" aria-label="Photo of two bulldogs looking up"></div><svg class="paw red" aria-hidden="true"><use href="#paw"/></svg><svg class="paw gold" aria-hidden="true"><use href="#paw"/></svg><div class="card-name">Services Name</div><svg class="paw green" aria-hidden="true"><use href="#paw"/></svg></div>
  <div class="card"><div class="card-photo" role="img" aria-label="Photo of two bulldogs looking up"></div><svg class="paw red" aria-hidden="true"><use href="#paw"/></svg><svg class="paw gold" aria-hidden="true"><use href="#paw"/></svg><div class="card-name">Services Name</div><svg class="paw green" aria-hidden="true"><use href="#paw"/></svg></div>
  <div class="card"><div class="card-photo" role="img" aria-label="Photo of two bulldogs looking up"></div><svg class="paw red" aria-hidden="true"><use href="#paw"/></svg><svg class="paw gold" aria-hidden="true"><use href="#paw"/></svg><div class="card-name">Services Name</div><svg class="paw green" aria-hidden="true"><use href="#paw"/></svg></div>
  <div class="card"><div class="card-photo" role="img" aria-label="Photo of two bulldogs looking up"></div><svg class="paw red" aria-hidden="true"><use href="#paw"/></svg><svg class="paw gold" aria-hidden="true"><use href="#paw"/></svg><div class="card-name">Services Name</div><svg class="paw green" aria-hidden="true"><use href="#paw"/></svg></div>
  <div class="card"><div class="card-photo" role="img" aria-label="Photo of two bulldogs looking up"></div><svg class="paw red" aria-hidden="true"><use href="#paw"/></svg><svg class="paw gold" aria-hidden="true"><use href="#paw"/></svg><div class="card-name">Services Name</div><svg class="paw green" aria-hidden="true"><use href="#paw"/></svg></div>
  <div class="card"><div class="card-photo" role="img" aria-label="Photo of two bulldogs looking up"></div><svg class="paw red" aria-hidden="true"><use href="#paw"/></svg><svg class="paw gold" aria-hidden="true"><use href="#paw"/></svg><div class="card-name">Services Name</div><svg class="paw green" aria-hidden="true"><use href="#paw"/></svg></div>
</div>
<div class="abs contact-photo" role="img" aria-label="Photo of two bulldogs resting side by side"></div>
<svg class="abs wave" style="top:1750px" width="1200" height="130" viewBox="0 1750 1200 130">
  <path d="M0 1750 L1200 1750 L1200 1775 C1050 1800 900 1835 700 1810 C500 1785 380 1770 250 1790 C150 1805 60 1840 0 1858 Z" fill="var(--yellow)"/>
</svg>
<svg class="abs wave" style="top:2120px" width="1200" height="180" viewBox="0 2120 1200 180">
  <path d="M0 2218 C200 2205 450 2170 700 2165 C900 2160 1050 2150 1200 2135 L1200 2300 L0 2300 Z" fill="var(--footer)"/>
</svg>
<h2 class="abs contact-title">GET IN TOUCH</h2>
<div class="abs field name">Your name</div>
<div class="abs field email">Your email</div>
<div class="abs submit">SUBMIT</div>
<div class="abs info info-mail"><svg class="paw gold" aria-hidden="true"><use href="#paw"/></svg><svg class="paw green" aria-hidden="true"><use href="#paw"/></svg><svg class="paw red" aria-hidden="true"><use href="#paw"/></svg><h3>MAIL</h3><p>PO Box 482<br>Harbor Ridge MD 21700</p></div>
<div class="abs info info-hours"><svg class="paw gold" aria-hidden="true"><use href="#paw"/></svg><svg class="paw green" aria-hidden="true"><use href="#paw"/></svg><svg class="paw red" aria-hidden="true"><use href="#paw"/></svg><h3>HOURS</h3><p>Weekdays:<br>10am - 4pm WST</p></div>
<div class="abs info info-phone"><svg class="paw gold" aria-hidden="true"><use href="#paw"/></svg><svg class="paw green" aria-hidden="true"><use href="#paw"/></svg><svg class="paw red" aria-hidden="true"><use href="#paw"/></svg><h3>PHONE</h3><p>0400 555 017</p></div>
<div class="abs info info-email"><svg class="paw gold" aria-hidden="true"><use href="#paw"/></svg><svg class="paw green" aria-hidden="true"><use href="#paw"/></svg><svg class="paw red" aria-hidden="true"><use href="#paw"/></svg><h3>EMAIL</h3><p>hi@standtall.org</p></div>
<div class="abs divider"></div>
<p class="abs copyright">© 2018 | STAND TALL RESCUE</p>
<div class="abs social"><span></span><span></span><span></span><span></span></div>
</body>
</html>
```